TORVO BEARD BALM LABEL DESIGN

We need a label design for our new company Torvo beard balm. Our company used to be called Wandering Fern but we changed our name. We currently already have the logo with the old name, so it would be awesome if we can change the name to " Mr. Torvo" in cursive writing.
Rounded Top Circular Tin
60 mm X 20 mm
As for the label, I want it to say " Mr. Torvo Premium Beard Balm" and the words under the Man in suit. I would like the word "Mr. Torvo" to be in a cursive and go from shoulder to shoulder under the man in suit logo in replace of the previous name shown. I would also like the word "Premium Beard Balm" to be under the word " Mr. Torvo" in a smaller, NON-CURSIVE but very sleek font. All of this should be around the middle of the circular label.
The following words can be placed anywhere on the label where it's best suited with any nice looking, smaller font.
- All Natural Oils
- Fresh Cucumber and Black Licorice (Flavor of the balm)
- Aphrodisiac Scent
- 2 oz.
And lastly, I want the color of the label to have a BLACK background and all the words including the Man in suit logo, to be in SILVER. This is a must.
Thank you very much for viewing my description and hopefully you will take my project.
Cheers, Oswin.
Men with Beards
It Company

```html
<!DOCTYPE html>
<html lang="en">
<head>
<meta charset="utf-8">
<title>Mr Torvo — Premium Beard Balm Label</title>
<link rel="stylesheet" href="https://fonts.googleapis.com/css2?family=Josefin+Sans:wght@400;600&family=Lato:wght@400&display=swap">
<style>
  :root {
    --backdrop-light: #ffffff;
    --backdrop-dark: #dcdcdc;
    --label-black: #0d0d0d;
    --silver: #d2d2d2;
    --silver-bright: #f4f4f4;
    --silver-deep: #9c9c9c;
    --ink-dark: #222222;
  }
  html, body {
    margin: 0;
    padding: 0;
    width: 1200px;
    height: 900px;
    overflow: hidden;
  }
  .canvas {
    position: relative;
    width: 1200px;
    height: 900px;
    background: radial-gradient(ellipse at 50% 45%, var(--backdrop-light) 0%, #f1f1f1 45%, var(--backdrop-dark) 100%);
  }
  .tin-label {
    position: absolute;
    left: 320px;
    top: 170px;
    width: 560px;
    height: 560px;
    filter: drop-shadow(0 10px 18px rgba(0,0,0,0.18));
  }
  .arc-copy {
    font-family: "Josefin Sans", sans-serif;
    font-weight: 400;
    font-size: 10px;
    letter-spacing: 2.6px;
    fill: var(--silver);
  }
  .brand-name {
    font-family: "Josefin Sans", sans-serif;
    font-weight: 600;
    font-size: 34px;
    fill: var(--silver);
  }
  .product-line {
    font-family: "Josefin Sans", sans-serif;
    font-weight: 600;
    font-size: 10.5px;
    letter-spacing: 4px;
    fill: var(--silver-bright);
  }
  .flavour {
    font-family: "Lato", sans-serif;
    font-weight: 400;
    font-size: 13px;
    fill: var(--ink-dark);
  }
  .net-weight {
    font-family: "Lato", sans-serif;
    font-size: 8px;
    fill: var(--silver-deep);
  }
</style>
</head>
<body>
<main class="canvas">
  <svg class="tin-label" viewBox="0 0 320 320" xmlns="http://www.w3.org/2000/svg">
    <defs>
      <linearGradient id="silver-ribbon" x1="0" y1="0" x2="1" y2="1">
        <stop offset="0" stop-color="var(--silver-bright)"/>
        <stop offset="0.5" stop-color="#bdbdbd"/>
        <stop offset="1" stop-color="#ececec"/>
      </linearGradient>
      <linearGradient id="silver-tail" x1="0" y1="0" x2="0" y2="1">
        <stop offset="0" stop-color="#cfcfcf"/>
        <stop offset="1" stop-color="var(--silver-deep)"/>
      </linearGradient>
      <path id="top-arc" d="M 17,160 A 143 143 0 0 1 303,160"/>
    </defs>

    <circle class="label-disc" cx="160" cy="160" r="159" fill="var(--label-black)"/>

    <path class="label-ring" d="M 297.2,110.1 A 146 146 0 1 1 22.8,110.1"
          fill="none" stroke="var(--silver)" stroke-width="1.1"/>

    <text class="arc-copy">
      <textPath href="#top-arc" startOffset="27.5%" text-anchor="middle">ALL NATURAL OILS</textPath>
    </text>
    <text class="arc-copy">
      <textPath href="#top-arc" startOffset="72.5%" text-anchor="middle">APHRODISIAC SCENT</textPath>
    </text>
    <line class="arc-divider" x1="142" y1="15" x2="178" y2="15" stroke="var(--silver)" stroke-width="1"/>

    <g class="brand-mark">
      <circle cx="160" cy="64" r="28" fill="none" stroke="var(--silver)" stroke-width="1.5"/>
      <text class="brand-name" x="160" y="140" text-anchor="middle">Mr Torvo</text>
    </g>

    <text class="product-line" x="162" y="178" text-anchor="middle">PREMIUM BEARD BALM</text>

    <g class="flavour-ribbon">
      <polygon points="58,216 98,216 98,254 58,254 70,235" fill="url(#silver-tail)"/>
      <polygon points="262,216 222,216 222,254 262,254 250,235" fill="url(#silver-tail)"/>
      <polygon points="90,244 98,254 98,244" fill="#6e6e6e"/>
      <polygon points="230,244 222,254 222,244" fill="#6e6e6e"/>
      <rect x="90" y="202" width="140" height="42" fill="url(#silver-ribbon)"/>
      <rect x="93" y="205" width="134" height="36" fill="none" stroke="#7a7a7a" stroke-width="0.6"/>
      <text class="flavour" x="160" y="220" text-anchor="middle">Fresh Cucumber</text>
      <text class="flavour" x="160" y="236" text-anchor="middle">&amp; Black Licorice</text>
    </g>

    <g class="net-weight-badge">
      <circle cx="160" cy="293" r="14" fill="var(--label-black)" stroke="#5a5a5a" stroke-width="0.8"/>
      <text class="net-weight" x="160" y="296" text-anchor="middle">2oz.</text>
    </g>
  </svg>
</main>
</body>
</html>
```